Refrigeration & Air Conditioning modern and appealing

We want to design a business card that is modern and appealing using existing logo supplied

Front card
Residential Commercial Diary
RTA : AU071523
Licence L258907

Back card
Marcus Ovenly
Director
0491 352 406
info@frostvalecooling.com.au
www.frostvalecooling.com.au
• Air Conditioning
• Cool Rooms & Refrigeration
• Installation
• Service & Repair
• Preventative Maintenance

We offer 24/7 emergency service

```html
<!DOCTYPE html>
<html lang="en">
<head>
<meta charset="utf-8">
<title>Frostvale Business Card</title>
<link href="https://fonts.googleapis.com/css2?family=Montserrat:wght@400;500;600;700;800&display=swap" rel="stylesheet">
<style>
  :root {
    --stage: #3a3a3d;
    --purple: #a04fe0;
    --purple-light: #b182ec;
    --lavender: #b9b4fb;
    --ink: #0e0d10;
    --white: #ffffff;
    --rule: #9a9a9a;
  }
  * { margin: 0; padding: 0; box-sizing: border-box; }
  html, body { width: 1200px; height: 939px; overflow: hidden; }
  body {
    background: var(--stage);
    font-family: "Montserrat", sans-serif;
    position: relative;
  }
  .card {
    position: absolute;
    width: 520px;
    height: 318px;
    border-radius: 22px;
    overflow: hidden;
  }
  /* Front */
  .card-front {
    left: 90px; top: 110px;
    background: linear-gradient(200deg, var(--purple-light) 0%, var(--purple) 60%);
    color: var(--white);
  }
  .brand {
    position: absolute;
    left: 0; right: 0; top: 118px;
    display: flex; align-items: center; justify-content: center; gap: 14px;
  }
  .brand-dot {
    width: 34px; height: 34px; border-radius: 50%;
    background: var(--white);
    flex: none;
  }
  .brand-name {
    font-weight: 800; font-size: 44px; letter-spacing: 1px;
    color: var(--white);
    white-space: nowrap;
  }
  .front-footer {
    position: absolute;
    left: 0; right: 0; bottom: 26px;
    text-align: center;
    font-size: 12px; font-weight: 500;
  }
  /* Back */
  .card-back {
    left: 590px; top: 500px;
    background: var(--ink);
    color: var(--white);
  }
  .card-back::after {
    content: "";
    position: absolute; left: 0; right: 0; bottom: 0; height: 12px;
    background: linear-gradient(90deg, var(--purple), var(--lavender));
  }
  .back-brand {
    position: absolute; left: 26px; top: 90px;
    width: 190px;
    display: flex; align-items: center; gap: 9px;
  }
  .back-brand .brand-dot { width: 20px; height: 20px; background: var(--purple-light); }
  .back-brand .brand-name { font-size: 20px; letter-spacing: .5px; color: var(--purple-light); }
  .divider {
    position: absolute; left: 232px; top: 52px;
    width: 1px; height: 120px; background: var(--rule);
  }
  .contact { position: absolute; left: 250px; top: 48px; right: 16px; }
  .person-name {
    font-weight: 700; font-size: 21px; text-transform: uppercase;
    color: var(--purple-light); letter-spacing: .5px;
    white-space: nowrap;
  }
  .person-role { font-size: 12px; margin-bottom: 10px; }
  .contact-line {
    display: flex; align-items: center; gap: 7px;
    font-size: 11.5px; margin-top: 5px;
    white-space: nowrap;
  }
  .contact-line svg { width: 12px; height: 12px; fill: var(--lavender); flex: none; }
  .services {
    position: absolute; left: 0; right: 0; top: 198px;
    text-align: center;
  }
  .services-title {
    font-weight: 700; font-size: 13px; color: var(--purple-light);
    text-transform: uppercase; margin-bottom: 6px;
  }
  .services-list { font-size: 12.5px; line-height: 1.5; }
</style>
</head>
<body>
  <section class="card card-front">
    <div class="brand">
      <span class="brand-dot"></span>
      <span class="brand-name">FROSTVALE</span>
    </div>
    <p class="front-footer">RTA : AU071523 • Residential Commercial Diary • Licence L258907</p>
  </section>

  <section class="card card-back">
    <div class="back-brand">
      <span class="brand-dot"></span>
      <span class="brand-name">FROSTVALE</span>
    </div>
    <div class="divider"></div>
    <div class="contact">
      <h1 class="person-name">Marcus Ovenly</h1>
      <p class="person-role">Director</p>
      <p class="contact-line">
        <svg viewBox="0 0 24 24" aria-hidden="true"><path d="M6.6 10.8a15.2 15.2 0 0 0 6.6 6.6l2.2-2.2a1 1 0 0 1 1-.25 11.4 11.4 0 0 0 3.6.57 1 1 0 0 1 1 1V20a1 1 0 0 1-1 1A17 17 0 0 1 3 4a1 1 0 0 1 1-1h3.5a1 1 0 0 1 1 1c0 1.250.2 2.450.57 3.570a1 1 0 0 1-.25 1z"/></svg>
        0491 352 406
      </p>
      <p class="contact-line">
        <svg viewBox="0 0 24 24" aria-hidden="true"><path d="M2 5h20v14H2zm2 2v.5l8 5 8-5V7l-8 5z"/></svg>
        info@frostvalecooling.com.au
      </p>
      <p class="contact-line">
        <svg viewBox="0 0 24 24" aria-hidden="true"><path d="M12 2a10 10 0 1 0 0 20 10 10 0 0 0 0-20zm6.9 6h-3a15 15 0 0 0-1.3-4A8 8 0 0 1 18.9 8zM12 4c.8 1.1 1.5 2.5 1.9 4h-3.8c.4-1.5 1.1-2.9 1.9-4zM4.3 14a8 8 0 0 1 0-4h3.4a16 16 0 0 0 0 4zm.8 2h3a15 15 0 0 0 1.3 4 8 8 0 0 1-4.3-4zm3-8h-3a8 8 0 0 1 4.3-4 15 15 0 0 0-1.3 4zM12 20c-.8-1.1-1.5-2.5-1.9-4h3.8c-.4 1.5-1.1 2.9-1.9 4zm2.3-6H9.7a14 14 0 0 1 0-4h4.6a14 14 0 0 1 0 4zm.3 6a15 15 0 0 0 1.3-4h3a8 8 0 0 1-4.3 4zm1.7-6a16 16 0 0 0 0-4h3.4a8 8 0 0 1 0 4z"/></svg>
        www.frostvalecooling.com.au
      </p>
    </div>
    <div class="services">
      <p class="services-title">We offer 24/7 emergency service</p>
      <p class="services-list">• Air Conditioning • Cool Rooms &amp; Refrigeration • Installation<br>• Service &amp; Repair • Preventative Maintenance</p>
    </div>
  </section>
</body>
</html>
```